7th Annual Falcon Ridge Classic Flyer

Looking to design an updated eye catching flyer maybe with someone movement, sound, and color. Below is an attachment of the flyer I have used in the past. I need to add color, sound, and movement to the flyer. This is an advertisement for youth folk style wrestling. You may contact me directly at 252-381-4927 if you need additional information. I really like the colors music and movement in the video below.
https://www.vidloomer.com/watch?v=kQ7mTbLw2Ra

Target Market(s)

Youth Wrestling

Font styles to use
Serif

Colors
EB3D1F
EC4F4E
F09395
F8D3D4
FCEDEE

Requirements
Must have
• All information included on flyer.
Nice to have
• Color, sound, and movement

```html
<!DOCTYPE html>
<html lang="en">
<head>
<meta charset="utf-8">
<title>7th Annual Falcon Ridge Classic</title>
<link href="https://fonts.googleapis.com/css2?family=Rye&family=Great+Vibes&family=Bebas+Neue&family=Poppins:wght@400;600;700;800&family=Source+Sans+3:wght@400;600;700&display=swap" rel="stylesheet">
<style>
:root{
  --page:#dedede;
  --bark:#1f120d;
  --cocoa:#3a1f16;
  --rust:#6b3424;
  --rust-deep:#572a1d;
  --row:rgba(38,18,12,.55);
  --gold:#f6c445;
  --sand:#e8cf97;
  --amber:#f29b38;
  --peach:#f5b561;
  --cream:#fbf6e3;
  --ink:#3a1d14;
  --clay:#b86a3c;
  --white:#fff8ec;
}
*{margin:0;padding:0;box-sizing:border-box}
html,body{width:1200px;height:967px;overflow:hidden;background:var(--page)}
.flyer{position:absolute;left:241px;top:19px;width:1008px;height:1304px;transform:scale(.7125);transform-origin:0 0;overflow:hidden;
  background:radial-gradient(ellipse at 62% 28%,#8a5a2e 0%,#4a2a1a 38%,var(--bark) 75%);font-family:"Poppins",sans-serif;color:var(--white)}
.abs{position:absolute}
.hero-art{left:560px;top:180px;width:448px;height:520px;
  background:radial-gradient(ellipse at 30% 40%,#c9893e 0%,#7a4a26 40%,rgba(40,22,14,0) 75%)}
.edition{left:64px;top:52px;font-family:"Rye",serif;font-size:50px;color:var(--gold)}
.edition sup{font-size:26px;vertical-align:22px}
.title{left:60px;top:110px;font-family:"Rye",serif;font-size:86px;line-height:1;color:#fbe9c0;letter-spacing:1px;white-space:nowrap}
.script{left:70px;top:210px;font-family:"Great Vibes",cursive;font-size:118px;color:var(--white);line-height:1}
.org{left:735px;top:72px;width:220px;text-align:center;font-family:"Poppins",sans-serif;font-weight:700;color:var(--white)}
.org-mark{display:flex;align-items:center;justify-content:center;gap:10px;font-size:30px;margin-bottom:14px}
.org-mark span.dot{width:26px;height:26px;border-radius:50%;background:var(--white)}
.org-line{font-size:13px;line-height:1.25}
.datebox{left:64px;top:356px;width:118px;height:166px;background:var(--sand);color:var(--ink);text-align:center}
.datebox .day{font-family:"Bebas Neue",sans-serif;font-size:30px;margin-top:16px;line-height:1}
.datebox .num{font-family:"Rye",serif;font-size:78px;line-height:.95}
.datebox .mon{font-family:"Rye",serif;font-size:18px;letter-spacing:3px}
.yearbar{left:182px;top:356px;width:30px;height:166px;background:var(--rust);font-family:"Bebas Neue",sans-serif;font-size:30px;color:var(--sand);text-align:center;line-height:33px;padding-top:16px}
.label{font-family:"Bebas Neue",sans-serif;color:var(--amber);font-size:30px;line-height:1}
.info{font-weight:700;font-size:14.5px;line-height:1.1}
.tiny{font-size:11px;letter-spacing:3px;color:var(--peach);font-weight:600}
.pill{display:inline-block;background:var(--cream);color:var(--ink);border-radius:12px;font-weight:700;font-size:15px;padding:1px 12px}
.register{left:540px;top:496px;width:408px;height:30px;background:rgba(20,10,6,.7);border-radius:15px;display:flex;align-items:center}
.register .btn{background:var(--amber);color:var(--ink);font-family:"Bebas Neue",sans-serif;font-size:24px;border-radius:15px;padding:0 14px;height:30px;line-height:31px}
.register .url{font-weight:600;font-size:17px;letter-spacing:1px;margin-left:12px}
.reg-row{left:64px;display:flex;align-items:center;height:26px;white-space:nowrap}
.reg-row .name{width:176px;font-family:"Bebas Neue",sans-serif;font-size:24px}
.reg-row .arrow{width:0;height:0;border-left:6px solid var(--amber);border-top:6px solid transparent;border-bottom:6px solid transparent;margin-right:10px}
.reg-row .price{width:66px;height:22px;font-weight:700;font-size:16px;text-align:center;line-height:22px;margin-right:12px}
.reg-row .dl{width:88px;font-size:10.5px;letter-spacing:2px;font-weight:600;border-right:1px solid rgba(255,255,255,.3);margin-right:10px}
.reg-row .when{font-weight:700;font-size:12.5px;width:134px}
.reg-row .pill{font-size:11.5px;padding:0 8px}
.note{font-size:11.5px;font-weight:700;color:var(--amber);line-height:1.2}
.big{font-family:"Bebas Neue",sans-serif;font-size:36px;line-height:1}
.tear{left:0;width:1008px}
.mid{left:0;top:700px;width:1008px;height:360px;background:linear-gradient(180deg,var(--rust) 0%,var(--rust-deep) 100%)}
.div-title{font-family:"Poppins",sans-serif;font-weight:800;font-size:21px;color:var(--amber);letter-spacing:.5px}
.div-list{display:flex;flex-direction:column;gap:3px}
.div-row{background:var(--row);border-radius:3px;padding:2px 9px;font-family:"Source Sans 3",sans-serif;font-size:12.5px;line-height:1.2}
.div-row b{display:block;font-weight:700;font-size:13px}
.age{left:518px;top:920px;font-weight:800;font-size:13.5px;line-height:1.15}
.ageday{left:710px;top:916px;font-family:"Bebas Neue",sans-serif;font-size:40px;color:var(--amber)}
.rule{left:518px;top:984px;border-left:3px solid var(--amber);padding-left:10px;font-size:14px;line-height:1.2;width:430px}
.bottom{left:0;top:1050px;width:1008px;height:254px;background:var(--cream)}
.on-cream{color:var(--ink)}
.weigh{left:64px;top:1086px;width:440px;font-family:"Source Sans 3",sans-serif;font-size:12.5px;line-height:1.25}
.weigh h3{font-family:"Poppins",sans-serif;font-weight:800;font-size:21px;color:var(--clay);margin-bottom:2px;line-height:1.2}
.weigh .sm{font-size:11px;font-weight:400}
.ticks{list-style:none;margin-top:14px;font-weight:700;font-size:11px;line-height:1.3}
.ticks li{position:relative;padding-left:14px}
.ticks li:before{content:"";position:absolute;left:0;top:3px;width:8px;height:8px;border-radius:50%;background:var(--amber)}
.adm{left:518px;top:1080px;display:flex;align-items:center;line-height:1;height:50px}
.adm .t{font-weight:800;font-size:33px;color:var(--amber);letter-spacing:1px;margin-right:16px}
.adm .p{font-weight:800;font-size:44px}
.adm .p sup{font-size:22px;vertical-align:18px}
.adm .pp{font-weight:800;font-size:17px;line-height:.95;margin-left:4px}
.contact-lbl{left:518px;top:1140px;font-size:11.5px;letter-spacing:2.6px;font-weight:600;white-space:nowrap}
.contact{left:518px;top:1156px;display:flex;align-items:center;font-weight:800;font-size:28px;line-height:1.2;white-space:nowrap}
.contact svg{margin:0 4px 0 18px}
.hotels{left:518px;top:1212px;font-weight:800;font-size:16px;line-height:1.05}
.hotels span{font-weight:400;color:var(--clay)}
.hotel-list{left:708px;top:1204px;border-left:2px solid var(--amber);padding-left:24px;font-size:13px;line-height:1.3;display:grid;grid-template-columns:112px auto;column-gap:4px;white-space:nowrap}
.hotel-list .ph{font-weight:700}
</style>
</head>
<body>
<main class="flyer">
  <div class="abs hero-art" role="img" aria-label="Illustration of a helmeted ancient warrior standing before a sunset mountain landscape"></div>

  <div class="abs edition">7<sup>th</sup> Annual</div>
  <h1 class="abs title">FALCON RIDGE</h1>
  <div class="abs script">Classic</div>

  <div class="abs org">
    <div class="org-mark"><span class="dot"></span>CPWL</div>
    <div class="org-line">CAROLINA PIEDMONT<br>WRESTLING LEAGUE</div>
  </div>

  <div class="abs datebox"><div class="day">SATURDAY</div><div class="num">25</div><div class="mon">JANUARY</div></div>
  <div class="abs yearbar">2<br>0<br>2<br>5</div>

  <div class="abs label" style="left:253px;top:356px">LOCATION ▸</div>
  <div class="abs info" style="left:361px;top:358px">Harborview Expo<br>Center 418 Lakemont Blvd<br>SW Greenville, NC 27834</div>

  <div class="abs label" style="left:253px;top:402px">TIME</div>
  <div class="abs info" style="left:253px;top:432px">4U, 6U, 8U, 10U</div>
  <div class="abs" style="left:253px;top:448px"><span class="tiny">WRESTLING STARTS AT</span> <span class="pill">8:30 am</span></div>
  <div class="abs info" style="left:253px;top:482px">12U, Middle School, &amp; High School</div>
  <div class="abs" style="left:253px;top:503px"><span class="tiny">WRESTLING STARTS AT</span> <span class="pill">8:30 am</span></div>

  <div class="abs register"><span class="btn">REGISTER AT</span><span class="url">@ www.matbracket.com</span></div>

  <div class="abs reg-row" style="top:554px"><span class="name">EARLY REGISTRATION</span><span class="arrow"></span><span class="price" style="background:#8a4a33">$30.00</span><span class="dl">DEADLINE IS</span><span class="when">January 19, 2025 at</span><span class="pill">11:59PM</span></div>
  <div class="abs reg-row" style="top:591px"><span class="name">REGULAR REGISTRATION</span><span class="arrow"></span><span class="price" style="background:#b5653f">$40.00</span><span class="dl">DEADLINE IS</span><span class="when">January 22, 2025 at</span><span class="pill">11:59PM</span></div>
  <div class="abs reg-row" style="top:627px"><span class="name">LATE REGISTRATION</span><span class="arrow"></span><span class="price" style="background:var(--amber);color:var(--ink)">$50.00</span><span class="dl">DEADLINE IS</span><span class="when">January 24, 2025 at</span><span class="pill">5:00PM</span></div>

  <div class="abs note" style="left:650px;top:554px">REGISTRATION IS<br>LIMITED TO THE FIRST</div>
  <div class="abs big" style="left:782px;top:552px">500 WRESTLERS</div>
  <div class="abs note" style="left:650px;top:603px">NON-CPWL CARD HOLDERS<br>WILL PAY AN ADDITIONAL</div>
  <div class="abs big" style="left:840px;top:602px">$5.00 <span style="font-size:13px;display:inline-block;line-height:1">AT<br>WEIGH-INS</span></div>

  <div class="abs mid"></div>
  <svg class="abs tear" style="top:682px" width="1008" height="30" viewBox="0 0 1008 30" aria-hidden="true"><path d="M0 12 L40 18 L80 8 L130 16 L180 6 L230 14 L290 9 L340 17 L400 7 L460 15 L520 10 L580 18 L640 8 L700 14 L760 6 L820 16 L880 9 L940 15 L1008 10 L1008 30 L0 30Z" fill="var(--rust)"/></svg>

  <h2 class="abs div-title" style="left:64px;top:718px">BOYS DIVISIONS</h2>
  <div class="abs div-list" style="left:64px;top:752px;width:434px">
    <div class="div-row"><b>4 &amp; Under</b>30, 40, 50, HWT</div>
    <div class="div-row"><b>6 &amp; Under</b>36, 40, 44, 48, 52, 56, 60, HWT</div>
    <div class="div-row"><b>8 &amp; Under</b>40, 44, 48, 52, 56, 60, 64, 68, 72, 76, 80, 84, 88, 92, HWT</div>
    <div class="div-row"><b>10 &amp; Under</b>52, 56, 60, 64, 68, 72, 76, 80, 84, 88, 92, 96, 100, 110, HWT</div>
    <div class="div-row"><b>12 &amp; Under</b>64, 68, 72, 76, 80, 84, 88, 92, 96, 100, 105, 110, 115, 120, 130, 140, 160, HWT</div>
    <div class="div-row"><b>Middle School</b>72, 76, 80, 88, 92, 96, 100, 105, 110, 115, 120, 130, 140, 160, 210, HWT</div>
    <div class="div-row"><b>High School</b>106, 113, 120, 126, 132, 138, 144, 150, 157, 165, 175, 190, 215, HWT</div>
  </div>

  <h2 class="abs div-title" style="left:513px;top:718px">GIRLS&nbsp; DIVISIONS</h2>
  <div class="abs div-list" style="left:513px;top:752px;width:435px">
    <div class="div-row" style="padding:9px">K-5 - 36, 40, 44, 48, 60, 64, 68, 72, 76, 80, 84, 88, 92, 96, 100, 110, 120, HWT</div>
    <div class="div-row" style="padding:9px;height:72px"><b>Middle School</b>72, 76, 83, 90, 98, 106, 113, 120, 126, 132, 138, 145, 152, 160, 170, 182, 190, 220, HWT</div>
    <div class="div-row" style="padding:4px 9px"><b>Women's High School</b>100, 107, 114, 120, 126, 132, 145, 152, 165, 185, HWT</div>
  </div>

  <div class="abs age">*AGE IS BASED UPON<br>WRESTLER'S AGE AS OF</div>
  <div class="abs ageday">DECEMBER 31, 2024</div>
  <div class="abs rule">Tournament director has the right to combine weight classes if deemed necessary.</div>

  <div class="abs bottom"></div>
  <svg class="abs tear" style="top:1034px" width="1008" height="26" viewBox="0 0 1008 26" aria-hidden="true"><path d="M0 10 L50 16 L100 6 L160 14 L220 8 L280 16 L340 6 L400 13 L460 7 L520 15 L580 5 L640 14 L700 8 L760 16 L820 7 L880 13 L940 6 L1008 12 L1008 26 L0 26Z" fill="var(--cream)"/></svg>

  <section class="abs weigh on-cream">
    <h3>WEIGH-INS</h3>
    <div><b>January 24, 2025 – 5:00 pm to 7:00 pm</b> <span class="sm">(Early Weigh-ins - $10 cash due at scale)</span></div>
    <div><b>January 25, 2025 – 6:00 am to 7:30 am</b> <span class="sm">(4U, 6U, 8U, 10U)</span></div>
    <div><b>January 25, 2025 – 11:00 am to 12:00 pm</b> <span class="sm">(12 &amp; Under, MS, &amp; High School)</span></div>
    <ul class="ticks">
      <li>Tenths are waived/dropped at weigh-ins. Satellite weigh-ins will not be allowed.</li>
      <li>High School Divisions are given 2 lbs. growth allowance.</li>
      <li>Custom medals will be given to the top 3 individual finishers in each bracket.</li>
      <li>Custom Awards will be awarded to the top 4 teams. Referee decisions will be final.</li>
      <li>Cedar Run Athletics is not responsible for accidents, injuries, or theft during<br>the tournament.</li>
    </ul>
  </section>

  <div class="abs adm on-cream"><span class="t">ADMISSION</span><span class="p"><sup>$</sup>10.00</span><span class="pp">PER<br>PERSON</span></div>
  <div class="abs contact-lbl on-cream">FOR MORE INFORMATION, CONTACT TOURNAMENT DIRECTOR</div>
  <div class="abs contact on-cream">Dale Corwin
    <svg width="28" height="28" viewBox="0 0 24 24" aria-hidden="true"><circle cx="12" cy="12" r="10.5" fill="none" stroke="var(--ink)" stroke-width="2"/><path d="M8 7c1-1 2 0 2.6 1.2.5 1-.4 1.4-.6 2 .6 1.4 1.6 2.4 3 3 .6-.2 1-1.1 2-.6C16.2 13.2 17 14 16 15c-1.5 1.6-4.3.4-6.3-1.7C7.6 11.3 6.4 8.5 8 7z" fill="var(--ink)"/></svg>(252) 381-4927</div>
  <div class="abs hotels on-cream"><span>HOTELS</span><br>AVAILABLE ON-SITE</div>
  <div class="abs hotel-list on-cream">
    <span>Riverside Suites</span><span class="ph">☏ (252) 555-0181</span>
    <span>Maple Lodge Inn</span><span class="ph">☏ (252) 555-0147</span>
    <span>Crestway Hotel</span><span class="ph">☏ (252) 555-0129</span>
  </div>
</main>
</body>
</html>
```